BrimKeel Limited needs a business card design

We need a business card design that reflects both professionalism and innovation and captures our brand identity. We provide online enterprise solutions to HR and executive management. We would like to use the colors in our logo (Blue and Orange). See attached file.

We would like a more creative design than the existing attached business card but maintain the same information on it.

To see our products site, please visit www.brimkeel.example which reflects more our identity
Updates

Please see our site: www.brimkeel.example, not www.brimkeel.example.co.uk for our colors and look and feel

Target Market(s)

Senior Executives

Industry/Entity Type

Business

Requirements
Must have
• Logo and use of logo colors
Nice to have
• Icons
Should not have
• Images

```html
<!DOCTYPE html>
<html lang="en">
<head>
<meta charset="utf-8">
<title>BrimKeel Limited – Business Card</title>
<link rel="stylesheet" href="https://fonts.googleapis.com/css2?family=Open+Sans:wght@400;600&family=Questrial&display=swap">
<style>
  :root {
    --brand-blue: #1f6db3;
    --brand-orange: #e0552b;
    --brand-orange-light: #ef7a4a;
    --card-white: #fbfbfb;
    --backdrop: #4a4d4f;
    --ink-white: #ffffff;
  }
  * { box-sizing: border-box; margin: 0; padding: 0; }
  html, body {
    width: 1200px; height: 900px; overflow: hidden;
    background: var(--backdrop);
    font-family: "Open Sans", Arial, sans-serif;
  }
  .canvas { position: relative; width: 1200px; height: 900px; }
  .card {
    position: absolute; left: 280px;
    width: 640px; height: 366px;
    background: var(--card-white);
    overflow: hidden;
    box-shadow: 0 10px 30px rgba(0,0,0,.35);
  }
  .card--back  { top: 64px; }
  .card--front { top: 470px; }

  .company-name {
    position: absolute;
    font-family: "Open Sans", Arial, sans-serif;
    font-weight: 600; color: var(--brand-blue);
    line-height: 1; white-space: nowrap;
  }

  /* Back */
  .back__name { left: 0; right: 0; top: 140px; text-align: center; font-size: 56px; }
  .back__url {
    position: absolute; left: 0; right: 0; top: 262px; text-align: center;
    font-size: 16px; font-weight: 600; color: var(--brand-orange);
  }
  .back__url-tld { color: var(--brand-orange-light); }

  /* Front */
  .front__band { position: absolute; inset: 0; width: 640px; height: 366px; }
  .front__name { left: 120px; top: 92px; font-size: 50px; }
  .front__holder {
    position: absolute; right: 22px; top: 20px; text-align: right;
    font-family: "Questrial", Arial, sans-serif;
  }
  .front__person { color: var(--brand-blue); font-size: 17px; letter-spacing: .5px; }
  .front__role { color: var(--brand-orange); font-size: 12px; }

  .contact {
    position: absolute; display: flex; flex-direction: column; align-items: center;
    color: var(--ink-white); font-size: 11.5px; line-height: 1.4; text-align: center;
    white-space: nowrap;
  }
  .contact__icon {
    width: 48px; height: 48px; border-radius: 50%;
    background: var(--ink-white); border: 3px solid var(--brand-orange);
    display: flex; align-items: center; justify-content: center;
    margin-bottom: 14px;
  }
  .contact__icon svg { width: 26px; height: 26px; }
  .contact--address { left: 0;     top: 183px; width: 200px; }
  .contact--phone   { left: 195px; top: 159px; width: 140px; }
  .contact--web     { left: 390px; top: 126px; width: 200px; }
</style>
</head>
<body>
<main class="canvas">

  <section class="card card--back" aria-label="Business card, back">
    <p class="company-name back__name">BrimKeel</p>
    <p class="back__url">www.brimkeel.example<span class="back__url-tld">.co.uk</span></p>
  </section>

  <section class="card card--front" aria-label="Business card, front">
    <svg class="front__band" viewBox="0 0 640 366" preserveAspectRatio="none" aria-hidden="true">
      <polygon points="0,222 640,128 640,366 0,366" fill="var(--brand-blue)"/>
    </svg>

    <div class="front__holder">
      <p class="front__person">Mara Velden</p>
      <p class="front__role">Managing Director</p>
    </div>

    <p class="company-name front__name">BrimKeel</p>

    <div class="contact contact--address">
      <span class="contact__icon">
        <svg viewBox="0 0 24 24"><path d="M12 2a7 7 0 0 0-7 7c0 5 7 13 7 13s7-8 7-13a7 7 0 0 0-7-7z" fill="var(--brand-blue)"/><circle cx="12" cy="9" r="2.6" fill="#fff"/></svg>
      </span>
      <p>BrimKeel Limited</p>
      <p>1406 Harrow House,</p>
      <p>12 Example St, London, W1A 0AA</p>
    </div>

    <div class="contact contact--phone">
      <span class="contact__icon">
        <svg viewBox="0 0 24 24"><path d="M6.6 3.5l3 3.2-1.8 2.1c1 2.2 2.7 3.9 4.9 5l2.1-1.8 3.2 3-1.6 3.2C10.6 18 5.9 13.3 3.8 7.5z" fill="var(--brand-blue)"/></svg>
      </span>
      <p>+44 20 7946 0123</p>
      <p>+1 323 555 0142</p>
      <p>+96170000123</p>
    </div>

    <div class="contact contact--web">
      <span class="contact__icon">
        <svg viewBox="0 0 24 24" fill="none" stroke="var(--brand-blue)" stroke-width="1.6"><circle cx="12" cy="12" r="9"/><ellipse cx="12" cy="12" rx="4" ry="9"/><path d="M3 12h18M4.5 7.5h15M4.5 16.5h15"/></svg>
      </span>
      <p>mvelden@brimkeel.example.co.uk</p>
      <p>www.brimkeel.example.co.uk</p>
    </div>
  </section>

</main>
</body>
</html>
```